Make my Savory Fungi Strips sell!!

Design for a new mushroom jerky product.
The meatiest (no) beef jerky ever!!
Bite it! Rip it! Tear it! Chew it! There is nothing meatier! Not even meat!
Please use our company logo (supplied) somewhere on the package. It does not have to be the focus. Just anywhere in the design.
Not sure if I want to focus on the plant based, healthy, clean - eating design or a masculine, taste based, BBQ, design. Surprise me!
Will be used on a stand up pouch, with a window.

Target Market(s)

Jerky lovers. Plant based connoisseurs. Vegans. Millenials. People that want a true meat experience without the cruelty.

Requirements
Must have
• Verdant Grove Foods logo.
Nice to have
• Mushrooms, shiitake, nature, muscles, happy cows?,
Should not have
• The word vegan. Stick to Plant Based.

```html
<!DOCTYPE html>
<html lang="en">
<head>
<meta charset="utf-8">
<title>Savory Fungi Strips – Pouch Front</title>
<link href="https://fonts.googleapis.com/css2?family=Big+Shoulders+Display:wght@500&family=Roboto:wght@700&display=swap" rel="stylesheet">
<style>
  :root {
    --bg: #ffffff;
    --pouch: #f7f7f6;
    --brown: #4a2610;
    --brown-dark: #3b1d0b;
    --green: #7ab72f;
    --tan: #b09a80;
    --tan-light: #d8cbbb;
  }
  html, body {
    margin: 0;
    width: 800px;
    height: 1200px;
    overflow: hidden;
    background: var(--bg);
  }
  .canvas {
    position: relative;
    width: 800px;
    height: 1200px;
  }
  .pouch-front {
    position: absolute;
    left: 150px;
    top: 210px;
    width: 490px;
    height: 780px;
    background: var(--pouch);
    overflow: hidden;
  }
  .band-top {
    position: absolute;
    left: 0; top: 0;
    width: 100%;
    height: 95px;
    background: linear-gradient(to bottom, var(--brown-dark) 0%, var(--brown) 70%, rgba(74,38,16,0) 100%);
  }
  .band-bottom {
    position: absolute;
    left: 0; bottom: 0;
    width: 100%;
    height: 28px;
    background: linear-gradient(to top, var(--brown) 60%, rgba(74,38,16,0) 100%);
    z-index: 1;
  }
  .mushroom-art {
    position: absolute;
    left: 30px;
    top: 590px;
    width: 430px;
    height: 175px;
    background: linear-gradient(to bottom, rgba(216,203,187,0) 0%, var(--tan-light) 35%, var(--tan) 100%);
    border-radius: 60px 60px 0 0;
    z-index: 0;
  }
  .company-name {
    position: absolute;
    left: 50px;
    top: 162px;
    margin: 0;
    font-family: 'Roboto', Arial, sans-serif;
    font-weight: 700;
    font-size: 19px;
    color: var(--green);
    letter-spacing: 0.2px;
    z-index: 2;
  }
  .brand-mark {
    position: absolute;
    left: 335px;
    top: 150px;
    width: 100px;
    height: 100px;
    border-radius: 50%;
    background: var(--green);
    z-index: 2;
  }
  .product-title {
    position: absolute;
    left: 48px;
    top: 192px;
    margin: 0;
    font-family: 'Big Shoulders Display', 'Arial Narrow', sans-serif;
    font-weight: 500;
    font-size: 150px;
    line-height: 140px;
    color: var(--brown);
    letter-spacing: 2px;
    transform: scaleX(0.85);
    transform-origin: left top;
    z-index: 2;
  }
  .product-title span { display: block; }
  .taglines {
    position: absolute;
    right: 72px;
    top: 478px;
    margin: 0;
    padding: 0;
    list-style: none;
    text-align: right;
    font-family: 'Roboto', Arial, sans-serif;
    font-weight: 700;
    font-size: 22px;
    line-height: 32px;
    color: var(--green);
    z-index: 2;
  }
  .slogan {
    position: absolute;
    left: 0;
    width: 100%;
    top: 698px;
    margin: 0;
    text-align: center;
    font-family: 'Roboto', Arial, sans-serif;
    font-weight: 700;
    font-size: 13px;
    color: var(--brown);
    z-index: 2;
  }
  .net-weight {
    position: absolute;
    left: 0;
    width: 100%;
    top: 728px;
    margin: 0;
    text-align: center;
    font-family: 'Roboto', Arial, sans-serif;
    font-weight: 700;
    font-size: 20px;
    color: var(--brown-dark);
    word-spacing: 6px;
    z-index: 2;
  }
</style>
</head>
<body>
<div class="canvas">
  <div class="pouch-front">
    <div class="band-top"></div>
    <div class="mushroom-art" role="img" aria-label="Cluster of mushrooms growing upward from the base of the pouch"></div>

    <p class="company-name">VERDANT GROVE FOODS</p>
    <div class="brand-mark" aria-hidden="true"></div>

    <h1 class="product-title">
      <span>SAVORY</span>
      <span>FUNGI</span>
      <span>STRIPS</span>
    </h1>

    <ul class="taglines">
      <li>BITE IT!</li>
      <li>RIP IT!</li>
      <li>TEAR IT!</li>
      <li>CHEW IT!</li>
    </ul>

    <p class="slogan">THERE IS NOTHING MEATIER! NOT EVEN MEAT!</p>
    <p class="net-weight">NET WT. 2.2 oz (62 g)</p>

    <div class="band-bottom"></div>
  </div>
</div>
</body>
</html>
```